Business Card Design Project

I am a Chiropractor that is looking for a new business card.  Our logo was slightly changed lately, therefore need a new, more professional look.
We are a modern, non-stuffy chiropractic office.  Want a contemporary look that will let people know this is not your typical doctors office.  Our logo is red, and contains the name of our business: realign.  The u in the logo is green, stressing the most important part of our business: "u"

Target Market(s)
moderate to upper income bracket, family friendly
www.realignspine.example
Gordon Pell
Family Chiropractor
412 Birch Ave
Pinewood, TX 78000
512.555.0147 phone
512.555.0148 fax
Industry/Entity Type
Business
Requirements
Must have
- www.realignspine.example
Gordon Pell
Family Chiropractor
412 Birch Ave
Pinewood, TX 78000
512.555.0147 phone
512.555.0148 fax

```html
<!DOCTYPE html>
<html lang="en">
<head>
<meta charset="utf-8">
<title>realign – business card</title>
<link rel="stylesheet" href="https://fonts.googleapis.com/css2?family=Source+Sans+3:wght@400;600&display=swap">
<style>
  :root {
    --red: #e6302a;
    --red-light: #f2604f;
    --red-deep: #d4221d;
    --green: #5cb947;
    --blush: #f6c9c4;
    --paper: #ffffff;
    --paper-tint: #fdf3f2;
    --ink: #4a4a4a;
    --stage: #ecebea;
  }
  * { margin: 0; padding: 0; box-sizing: border-box; }
  html, body { width: 1200px; height: 955px; overflow: hidden; }
  body {
    background: var(--stage);
    font-family: "Source Sans 3", "Myriad Pro", sans-serif;
    position: relative;
  }
  .card {
    position: absolute;
    left: 250px;
    width: 700px;
    height: 400px;
    border-radius: 30px;
    overflow: hidden;
    box-shadow: 0 6px 18px rgba(0,0,0,0.18);
  }
  .card--back { top: 40px; }
  .card--front { top: 515px; background: linear-gradient(180deg, var(--paper) 60%, var(--paper-tint)); }
  .card-shapes { position: absolute; inset: 0; }

  .brand {
    position: absolute;
    display: flex;
    align-items: center;
    gap: 14px;
    color: var(--paper);
    font-weight: 400;
    line-height: 1;
  }
  .brand-dot {
    border-radius: 50%;
    background: var(--paper);
  }
  .card--front .brand { left: 44px; top: 46px; font-size: 64px; }
  .card--front .brand-dot { width: 20px; height: 20px; }
  .card--back .brand { left: 50%; top: 50%; transform: translate(-50%, -60%); font-size: 96px; }
  .card--back .brand-dot { width: 28px; height: 28px; }

  .practice {
    position: absolute;
    left: 44px;
    top: 218px;
    color: var(--red);
    font-size: 18px;
    line-height: 1.15;
  }
  .contact-list {
    position: absolute;
    left: 44px;
    top: 272px;
    list-style: none;
    color: var(--ink);
    font-size: 17px;
    line-height: 1.25;
  }
  .contact-list li { display: flex; align-items: center; gap: 10px; }
  .contact-icon { width: 14px; height: 14px; flex: none; }

  .person {
    position: absolute;
    right: 56px;
    bottom: 48px;
    text-align: left;
  }
  .person-name { color: var(--red); font-size: 32px; font-weight: 400; line-height: 1.1; }
  .person-role { color: var(--green); font-size: 17px; margin-left: 24px; }
</style>
</head>
<body>

  <section class="card card--back" aria-label="Card back">
    <svg class="card-shapes" viewBox="0 0 700 400" preserveAspectRatio="none">
      <defs>
        <linearGradient id="backRed" x1="0" y1="0" x2="0" y2="1">
          <stop offset="0" stop-color="#f04b3c"/>
          <stop offset="1" stop-color="#e22b24"/>
        </linearGradient>
      </defs>
      <rect class="back-pattern-area" width="700" height="372" fill="url(#backRed)" role="img" aria-label="Repeating wordmark pattern in light red"/>
      <rect y="372" width="700" height="10" fill="var(--blush)"/>
      <rect y="382" width="700" height="18" fill="var(--green)"/>
    </svg>
    <div class="brand"><span class="brand-dot"></span>realign</div>
  </section>

  <section class="card card--front" aria-label="Card front">
    <svg class="card-shapes" viewBox="0 0 700 400" preserveAspectRatio="none">
      <defs>
        <linearGradient id="frontRed" x1="0" y1="0" x2="0" y2="1">
          <stop offset="0" stop-color="var(--red-light)"/>
          <stop offset="0.35" stop-color="var(--red)"/>
          <stop offset="1" stop-color="var(--red-deep)"/>
        </linearGradient>
      </defs>
      <path class="header-band" d="M0 0 H700 V196 H392 L372 174 H0 Z" fill="url(#frontRed)"/>
      <path class="accent-stripe" d="M0 174 H372 L392 196 H0 Z" fill="var(--green)"/>
      <rect class="header-rule" y="196" width="700" height="5" fill="var(--blush)"/>
    </svg>

    <div class="brand"><span class="brand-dot"></span>realign</div>

    <p class="practice">Family Chiropractor<br>412 Birch Ave Pinewood, TX 78000</p>

    <ul class="contact-list">
      <li>
        <svg class="contact-icon" viewBox="0 0 14 14"><path d="M3 1 L5 1 L6 4 L4.5 5.5 Q6 8.5 8.5 9.5 L10 8 L13 9 L13 11 Q13 13 11 13 Q1 12 1 3 Q1 1 3 1 Z" fill="var(--red)"/></svg>
        <span>512.555.0147</span>
      </li>
      <li>
        <svg class="contact-icon" viewBox="0 0 14 14"><rect x="1" y="1" width="12" height="12" rx="2" fill="var(--red)"/><rect x="4" y="3" width="6" height="3" fill="#fff"/><rect x="4" y="8" width="6" height="2" fill="#fff"/></svg>
        <span>512.555.0148</span>
      </li>
      <li>
        <svg class="contact-icon" viewBox="0 0 14 14"><rect x="1" y="3" width="12" height="8" rx="1" fill="var(--red)"/><path d="M1.5 3.5 L7 8 L12.5 3.5" stroke="#fff" stroke-width="1.2" fill="none"/></svg>
        <span>info@realignspine.example</span>
      </li>
      <li>
        <svg class="contact-icon" viewBox="0 0 14 14"><circle cx="7" cy="7" r="6" fill="var(--red)"/><ellipse cx="7" cy="7" rx="2.6" ry="6" stroke="#fff" stroke-width="1" fill="none"/><path d="M1 7 H13" stroke="#fff" stroke-width="1"/></svg>
        <span>www.realignspine.example</span>
      </li>
    </ul>

    <div class="person">
      <p class="person-name">Gordon Pell</p>
      <p class="person-role">General Manager</p>
    </div>
  </section>

</body>
</html>
```